Visitenkarte für Geschäftsführer von lumenrat.de
Zielgruppe
lumenrat.de ist ein Ratgeber-Portal, das die Fragen von Usern über Computer, Internet und Technik beantwortet. Vermarktet wir die Webseite von der brisolkan UG (haftungsbeschränkt).
Aufgabenstellung
Diesem Auftrag habe ich ein Beispiel angehangen, wie ich mir eine Visitenkarte vorstelle. Ziemlich genau so soll die Visitenkarte nachgeahmt werden - allerdings mit einem anderen Orange. Es soll sowohl eine Vorder- als auch eine Rückseite geben.
Farbgestaltung:
Orange vom beigefügten Logo, schwarz, grau, weiß
Vorderseite (dunkel):
Logo von lumenrat.de
www.lumenrat.de
Begriffe wie
- SEO
- Marketer
- Webmaster
- Schlagzeuger
- Hardware
- Software
- Online
- Mobile
- Ratgeber
- Anleitungen
etc.
Rückseite (hell):
Geschäftsführer und Chefredakteur
Bitte orientiert euch wirklich sehr genau an der Beispiel-Visitenkarte.

```html
<!DOCTYPE html>
<html lang="de">
<head>
<meta charset="utf-8">
<title>lumenrat.de – Visitenkarte</title>
<link href="https://fonts.googleapis.com/css2?family=Arimo:wght@400;700&family=Archivo+Black&family=Roboto:wght@300&display=swap" rel="stylesheet">
<style>
  :root {
    --stage: #d9d9d7;
    --card-light: #f4f4f2;
    --card-dark: #151515;
    --orange: #f07c12;
    --orange-deep: #d9650a;
    --ink: #111111;
    --grey-text: #3a3a3a;
    --term-strong: #2e2e2e;
    --term-soft: #3a3a3a;
    --white: #ffffff;
  }
  * { margin: 0; padding: 0; box-sizing: border-box; }
  html, body { width: 1200px; height: 1037px; overflow: hidden; background: var(--stage); }
  body { position: relative; font-family: "Arimo", Arial, sans-serif; }

  .card {
    position: absolute;
    left: 170px;
    width: 860px;
    height: 490px;
    overflow: hidden;
    box-shadow: 0 3px 10px rgba(0,0,0,0.18);
  }

  /* Back side (light) */
  .card--back { top: 20px; background: var(--card-light); }
  .portrait-area {
    position: absolute; left: 40px; top: 40px; width: 330px; height: 330px;
    border-radius: 46% 54% 50% 50% / 52% 44% 56% 48%;
    background: radial-gradient(circle at 50% 40%, #2b2b2b 0%, #0d0d0d 60%, #000 100%);
  }
  .portrait {
    position: absolute; left: 140px; top: 80px; width: 130px; height: 140px;
    background: radial-gradient(ellipse at 50% 35%, #6a5a50 0%, #2a2522 55%, #111 100%);
  }
  .back-wordmark {
    position: absolute; left: 95px; top: 230px;
    font-weight: 700; font-size: 42px;
    color: var(--orange); letter-spacing: -1px;
  }
  .identity { position: absolute; left: 430px; top: 100px; }
  .identity__name { font-weight: 700; font-size: 34px; color: var(--ink); letter-spacing: 0.5px; }
  .identity__role { font-size: 17px; color: var(--grey-text); margin-top: 4px; }
  .contacts { position: absolute; left: 430px; top: 265px; list-style: none; }
  .contacts li {
    display: flex; align-items: center; gap: 14px; height: 34px;
    font-size: 20px; color: var(--ink); letter-spacing: 1px;
  }
  .contacts li.strong { font-weight: 700; }
  .contacts svg { width: 22px; height: 22px; flex: none; }

  /* Front side (dark) */
  .card--front { top: 527px; background: var(--card-dark); }
  .splash {
    position: absolute;
    background: radial-gradient(circle, var(--orange) 0%, var(--orange-deep) 70%, rgba(217,101,10,0) 100%);
    border-radius: 50%;
  }
  .splash--top { left: -60px; top: -70px; width: 300px; height: 200px; }
  .splash--bottom { right: -50px; bottom: -110px; width: 300px; height: 230px; }

  .front-logo { position: absolute; left: 60px; top: 190px; }
  .front-logo__name {
    font-weight: 700; font-size: 76px;
    color: var(--orange); letter-spacing: -2px; line-height: 1;
  }
  .front-logo__url {
    font-size: 24px; color: var(--white);
    margin-top: 10px; margin-left: 4px; letter-spacing: 1px;
  }

  .terms {
    position: absolute; right: 60px; top: 48px;
    display: flex; flex-direction: column; align-items: flex-end; gap: 6px;
    list-style: none; line-height: 1; white-space: nowrap;
  }
  .term { color: var(--term-soft); }
  .term--hero { font-family: "Archivo Black", "Arial Black", sans-serif; font-size: 84px; color: var(--term-strong); }
  .term--large { font-family: "Roboto", Arial, sans-serif; font-weight: 300; font-size: 44px; letter-spacing: 2px; }
  .term--medium { font-weight: 700; font-size: 30px; color: var(--term-strong); }
  .term--thin { font-family: "Roboto", Arial, sans-serif; font-weight: 300; font-size: 26px; letter-spacing: 3px; }
  .term--small { font-weight: 700; font-size: 22px; letter-spacing: 1px; color: var(--term-strong); }
  .term--small-thin { font-family: "Roboto", Arial, sans-serif; font-weight: 300; font-size: 22px; letter-spacing: 2px; }
</style>
</head>
<body>

<section class="card card--back" aria-label="Rückseite">
  <div class="portrait-area" role="img" aria-label="Schwarzer Farbklecks als Hintergrund für das Porträt"></div>
  <div class="portrait" role="img" aria-label="Porträtfoto des Geschäftsführers"></div>
  <div class="back-wordmark">lumenrat</div>

  <div class="identity">
    <p class="identity__name">Jonas Kellermann</p>
    <p class="identity__role">Geschäftsführer und Chefredakteur</p>
  </div>

  <ul class="contacts">
    <li class="strong">
      <svg viewBox="0 0 24 24" aria-hidden="true"><rect x="2" y="5" width="20" height="14" fill="none" stroke="#111" stroke-width="2"/><path d="M2 5l10 8 10-8" fill="none" stroke="#111" stroke-width="2"/></svg>
      jonas@lumenrat.de
    </li>
    <li>
      <svg viewBox="0 0 24 24" aria-hidden="true"><path d="M6 2c-2 1-3 3-2 6 2 6 6 11 12 14 3 1 5 0 6-2l-4-4-3 2c-3-2-5-4-7-7l2-3z" fill="#111"/></svg>
      01520 4861207
    </li>
    <li>
      <svg viewBox="0 0 24 24" aria-hidden="true"><rect x="7" y="2" width="10" height="20" rx="2" fill="#111"/><rect x="9" y="5" width="6" height="10" fill="#fff"/></svg>
      089 730418265
    </li>
    <li class="strong">
      <svg viewBox="0 0 24 24" aria-hidden="true"><circle cx="12" cy="12" r="10" fill="#111"/><path d="M2 12h20M12 2v20M4.5 6.5h15M4.5 17.5h15" stroke="#fff" stroke-width="1.3" fill="none"/><ellipse cx="12" cy="12" rx="4.5" ry="10" stroke="#fff" stroke-width="1.3" fill="none"/></svg>
      www.lumenrat.de
    </li>
  </ul>
</section>

<section class="card card--front" aria-label="Vorderseite">
  <div class="splash splash--top" role="img" aria-label="Oranger Farbspritzer oben links"></div>
  <div class="splash splash--bottom" role="img" aria-label="Oranger Farbspritzer unten rechts"></div>

  <ul class="terms">
    <li class="term term--hero">SEO</li>
    <li class="term term--large">WEBMASTER</li>
    <li class="term term--medium">MARKETER</li>
    <li class="term term--thin">SCHLAGZEUGER</li>
    <li class="term term--small">HARDWARE · SOFTWARE</li>
    <li class="term term--small-thin">ONLINE · MOBILE</li>
    <li class="term term--small">RATGEBER · ANLEITUNGEN</li>
  </ul>

  <div class="front-logo">
    <div class="front-logo__name">lumenrat</div>
    <div class="front-logo__url">www.lumenrat.de</div>
  </div>
</section>

</body>
</html>
```